Silver Needle (E-commerce) Website for Embroidery shop

Briefing:

Silver Needle is an online personalized embroidery shop targeting mainly three customer segments:
1) lovers and marring couples
2) close friends wishing to give unique gifts
3) moms with new born baby personalized gifts

These customers are being served through our three major business lines:
1) Bathrobes and towels with personalized embroidery
2) Embroidered pillows and cushions
3) baby gifts with costumed baby sets stitched

Requirements:

The business has been recently established with moderate variety of products introduced so far. The website must consists of four major pages; a home page and three pages for every single business line. All images necessary for the web design are shareable upon request for copyright reasons if necessary. Please post a few products in each page to make it easy for the employee to use as benchmarks to upload other products.

The website also should contain all items and buttons exist in any e-commerce website such as:

1- social links:
a. (Major) Instagram: https://www.pinloop.example/silver.needle.studio/
b. Twitter: https://chirpnet.example/Silver_Needle_
c. Facebook: https://www.friendwall.example/Silver.neddle.studio/
d. Snapchat: coming soon

2- Help:
a. Delivery & Returns (inside KSA)
I. Delivery:
- Rush: within 3 business days (SAR 90)
- Express: within 5 business days (SAR 65)
- Standard: 7-10 business days ( SAR 35)
II. Returns: We guarantee you will love our product. But if you don't like it, send it back to us within two days from delivery and we will donate it to a charity and return your money subject to our terms and conditions.

b. Contact:
- Email: Silver.needle.studio@mailbox.example
- (Mobile) Whats-app: +966 55 312 0976 (for quick response)

d. Warranty:
for only SAR 20 per product, we will give you a lifetime warranty over our German stitches

3- Payment options:
bank transfer, visa, MasterCard and PayPal

Remarks:

- This website is mainly aimed at customers in Saudi Arabia where some contents may not appeal to people from such country and results in your participation being excluded from the contest.

- You are the expert and if I am a webdesigner, I would have not posted this contest, so please use your our own judgment and creativity to come up with the best experience possible.

- Use our Instagram account as your first reference to understand our business as it is our major channel that has been used to reach our customers. Please don't use the pictures with poor quality as we will be replacing them with other images with better quality.

- We intend to have this website bilingual (i.e English and Arabic), so if you can translate it into Arabic, then we will pay you an extra $100 in addition to the contest price.

- If in doubt, please feel free to ask any question and suggestions are always encouraged and warm welcomed.

- If you succeed in this contest, you will be chosen as our ultimate Web designer. That means you will have a long relationship providing services to our customers under one of our businesses that aims at preparing start-up companies establishing their business.

Target Market(s)

1) lovers and marrying couples

Industry/Entity Type

Embroidery

Number of Pages Required

4 page

Font styles to use
Serif
Script

Colors

Designer to choose colors to be used in the design.

Requirements
Must have
• Requirements:
• The business has been recently established with moderate variety of products introduced so far. The website must consists of four major pages; a home page and three pages for every single business line. All images necessary for the web design are shareable upon request for copyright reasons if necessary. Please post a few products in each page to make it easy for the employee to use as benchmarks to upload other products.
• The Website must be also mobile use friendly!!!
• The website also should contain all items and buttons exist in any e-commerce website such as:
• 1- social links:
• a. (Major) Instagram: https://www.pinloop.example/silver.needle.studio/
• b. Twitter: https://chirpnet.example/Silver_Needle_
• c. Facebook: https://www.friendwall.example/Silver.neddle.studio/
• d. Snapchat: coming soon
• 2- Help:
• a. Delivery & Returns (inside KSA)
• I. Delivery:
• - Rush: within 3 business days (SAR 90)
• - Express: within 5 business days (SAR 65)
• - Standard: 7-10 business days ( SAR 35)
• II. Returns: We guarantee you will love our product. But if you don't like it, send it back to us within two days from delivery and we will donate it to a charity and return your money subject to our terms and conditions.
• b. Contact:
• - Email: Silver.needle.studio@mailbox.example
• - (Mobile) Whats-app: +966 55 312 0976 (for quick response)
• d. Warranty:
• for only SAR 20 per product, we will give you a lifetime warranty over our German stitches
• 3- Payment options:
• bank transfer, visa, MasterCard and PayPal
• Note: You will be responsible to upload the design to the website fully and ensure its integration and functionality.

```html
<!DOCTYPE html>
<html lang="en">
<head>
<meta charset="utf-8">
<title>Silver Needle – Personalized Embroidery</title>
<link rel="stylesheet" href="https://fonts.googleapis.com/css2?family=Prata&family=Open+Sans:wght@300;400;600&family=Nunito+Sans:wght@400;600&display=swap">
<style>
:root{
  --gold:#b9964f;
  --gold-dark:#9c7c3c;
  --topbar:#7f7f7f;
  --footer:#8a8a8a;
  --light:#eeeeee;
  --text:#333333;
  --muted:#8c8c8c;
  --white:#ffffff;
  --black:#000000;
}
*{box-sizing:border-box;margin:0;padding:0}
html,body{width:1200px;height:2782px;overflow:hidden}
body{position:relative;background:var(--white);font-family:"Open Sans",sans-serif;color:var(--text)}
a{color:inherit;text-decoration:none}
.abs{position:absolute}

/* top bar */
.topbar{left:0;top:0;width:1200px;height:46px;background:var(--topbar);color:var(--white);font-size:15px}
.lang{left:500px;top:13px;display:flex;align-items:center;gap:8px;font-size:12px}
.flag{width:26px;height:17px;display:inline-block}
.flag-sa{background:#1f7a3a}
.flag-uk{background:#283f8c}
.account-links{left:705px;top:0;height:46px;display:flex;align-items:center}
.account-links a{padding:0 13px;border-left:1px solid rgba(255,255,255,.4)}
.account-links a:first-child{border-left:none}
.cart{left:979px;top:0;width:121px;height:46px;background:var(--gold);display:flex;align-items:center;justify-content:center;gap:8px;font-size:16px}

/* nav */
.navbar{left:0;top:46px;width:1200px;height:110px;background:var(--white)}
.brand{left:110px;top:34px;font-family:"Prata",serif;font-size:36px;color:var(--gold)}
.menu{left:428px;top:46px;display:flex;gap:0}
.menu a{font-size:18px;color:#888;margin-right:42px;letter-spacing:.3px}
.menu a.active{color:#222}

/* hero */
.hero{left:0;top:156px;width:1200px;height:560px;background:linear-gradient(110deg,#7b5d8a 0%,#9a7fa6 28%,#e9e6ea 52%,#d8d3dc 70%,#f2f1f3 100%)}
.hero-badge{left:708px;top:215px;width:390px;height:390px;border-radius:50%;background:rgba(185,150,79,.93);display:flex;align-items:center;justify-content:center}
.hero-badge-ring{position:absolute;inset:10px;border:2px solid var(--white);border-radius:50%}
.hero-badge-body{position:relative;text-align:center;color:var(--white)}
.hero-badge h2{font-family:"Open Sans",sans-serif;font-weight:400;font-size:35px;line-height:1.2}
.hero-badge p{font-size:13px;line-height:1.6;margin-top:14px}
.btn-dark{display:inline-block;margin-top:22px;background:#5b4a2a;color:var(--white);font-size:15px;font-weight:600;padding:10px 32px;border-radius:22px}
.dots{left:551px;top:608px;display:flex;gap:9px}
.dots span{width:15px;height:15px;border-radius:50%;border:2px solid var(--white)}
.dots span.on{background:var(--white)}
.hero-wave{left:0;top:600px;width:1200px;height:140px}

/* welcome */
.welcome-title{left:0;top:728px;width:1200px;text-align:center;font-family:"Prata",serif;font-size:40px;color:#222}
.welcome-text{left:148px;top:800px;width:934px;text-align:center;font-size:18px;line-height:33px;color:var(--muted)}

/* audience circles */
.segment{width:322px;height:322px;border-radius:50%;display:flex;flex-direction:column;align-items:center;justify-content:center;text-align:center;box-shadow:0 28px 22px -22px rgba(0,0,0,.25)}
.segment h3{font-weight:400;font-size:22px;line-height:28px;margin:16px 0 20px}
.segment .btn-outline{font-size:15px;padding:7px 30px;border-radius:20px;border:2px solid currentColor}
.seg-couples{left:95px;top:957px;background:#ececec;color:#222;border:8px solid #f5f5f5}
.seg-couples .btn-outline{border-color:#666}
.seg-friends{left:436px;top:957px;background:var(--gold);color:var(--white);border:8px solid #e3e3e3}
.seg-moms{left:776px;top:957px;background:var(--black);color:var(--white);border:8px solid #e3e3e3}

/* products */
.products{left:0;top:1363px;width:1200px;height:540px;background:var(--light)}
.products-title{left:0;top:1402px;width:1200px;text-align:center;font-family:"Prata",serif;font-size:36px;color:#333}
.slider-arrows{left:1058px;top:1424px;display:flex;gap:20px}
.card{top:1473px;width:243px;height:349px;background:var(--white);border:1px solid #ddd}
.card-img{height:208px}
.card h4{font-family:"Nunito Sans",sans-serif;font-weight:400;font-size:19px;margin:24px 0 0 22px;color:#222}
.card .sub{font-size:11px;color:#999;margin:4px 0 0 22px}
.card-foot{position:absolute;left:22px;right:20px;bottom:22px;display:flex;justify-content:space-between;align-items:center}
.price{font-family:"Nunito Sans",sans-serif;font-size:23px;color:var(--gold)}
.btn-shop{font-size:14px;color:#666;border:1.5px solid #888;border-radius:18px;padding:5px 20px}

/* testimonials */
.testi-bg{left:0;top:1830px;width:1200px;height:520px}
.testi-title{left:0;top:1940px;width:1200px;text-align:center;font-family:"Prata",serif;font-size:37px;color:var(--white)}
.quote{top:2013px;width:450px;height:200px;border:3px solid var(--white);border-radius:16px;color:var(--white);padding:32px 44px 0 50px}
.quote p{font-size:15px;line-height:26px;position:relative}
.quote p .mark{font-family:"Prata",serif;font-size:30px;position:absolute;left:-24px;top:-6px}
.quote .author{margin-top:12px;font-size:15px;font-weight:600;display:flex;align-items:center;gap:16px}
.stars{letter-spacing:3px;font-size:18px;font-weight:400}
.arrow-big{top:2088px}

/* footer */
.footer{left:0;top:2300px;width:1200px;height:482px;background:var(--footer);color:var(--white)}
.fcol h5{font-weight:400;font-size:20px;letter-spacing:.3px;margin-bottom:18px}
.fcol li{list-style:none;font-size:13.5px;line-height:30.5px}
.contact-row{display:flex;gap:12px;font-size:14.5px;line-height:22px;margin-bottom:14px}
.newsletter-input{width:295px;height:37px;background:var(--white);color:#888;font-size:12px;padding:10px 16px;letter-spacing:.5px}
.btn-subscribe{display:inline-block;margin-top:11px;background:var(--gold);font-size:16px;padding:9px 30px}
.pay{display:flex;gap:14px;margin-top:24px}
.pay span{width:40px;height:26px;background:var(--white);border-radius:3px}
.divider{left:106px;top:2705px;width:996px;height:1px;background:rgba(255,255,255,.25)}
.copyright{left:0;top:2726px;width:1200px;text-align:center;font-size:13px;color:#c9c9c9}
</style>
</head>
<body>

<header class="abs topbar">
  <div class="abs lang">Language: <span class="flag flag-sa"></span><span class="flag flag-uk"></span></div>
  <nav class="abs account-links"><a href="#">My Account</a><a href="#">Register</a><a href="#">Log In</a></nav>
  <a class="abs cart" href="#">
    <svg width="24" height="20" viewBox="0 0 24 20" fill="none" stroke="#fff" stroke-width="2"><path d="M1 2h4l3 11h12l3-8H7"/><circle cx="10" cy="17" r="1.6"/><circle cx="18" cy="17" r="1.6"/></svg>
    0 items
  </a>
</header>

<div class="abs navbar">
  <a class="abs brand" href="#">Silver Needle</a>
  <nav class="abs menu">
    <a class="active" href="#">HOME</a><a href="#">ABOUT US</a><a href="#">PRODUCTS</a><a href="#">SHOP NOW</a><a href="#">WHY US</a><a href="#">CONTACT</a>
  </nav>
</div>

<section class="abs hero" role="img" aria-label="Photo of folded purple and white towels embroidered with names, tied with ribbons"></section>
<div class="abs hero-badge">
  <div class="hero-badge-ring"></div>
  <div class="hero-badge-body">
    <h2>Embroidered<br>Pillows &amp; Cushions</h2>
    <p>Aociosqu ad litora torquent per conubia<br>nostra per inceptos hymenaeos</p>
    <a class="btn-dark" href="#">Shop Now ›</a>
  </div>
</div>
<div class="abs dots"><span class="on"></span><span class="on"></span><span class="on"></span><span class="on"></span></div>
<svg class="abs hero-wave" viewBox="0 0 1200 140" preserveAspectRatio="none">
  <path d="M0,92 Q560,10 1200,62 L1200,140 L0,140 Z" fill="#d9d9d9"/>
  <path d="M0,112 Q600,28 1200,88 L1200,140 L0,140 Z" fill="#ffffff"/>
</svg>

<h1 class="abs welcome-title">Welcome to Silver Needle</h1>
<p class="abs welcome-text">ue et malesuada iaculis ipsum dui aliquet felis at cursus magna nisl nec elit Praesent elementum elit at tellus nec ultricies sit amet porttitor mattis enim In massa libero interdum nec interdum vel blandit sed nulla In ullamcorper est eget tempor cursus neque mi consectetuer mi a ultricies</p>

<div class="abs segment seg-couples">
  <svg width="80" height="76" viewBox="0 0 80 76" fill="none" stroke="#555" stroke-width="3"><circle cx="29" cy="50" r="20"/><circle cx="29" cy="50" r="14"/><circle cx="51" cy="50" r="20"/><circle cx="51" cy="50" r="14"/><path d="M40 22 C34 16 30 8 36 5 C39 3 40 6 40 8 C40 6 41 3 44 5 C50 8 46 16 40 22Z"/></svg>
  <h3>Lovers and<br>Marring Couples</h3>
  <a class="btn-outline" href="#">Click here</a>
</div>
<div class="abs segment seg-friends">
  <svg width="96" height="70" viewBox="0 0 96 70" fill="#fff"><path d="M48 22 C38 6 14 2 8 12 C2 24 26 34 44 30Z M48 22 C58 6 82 2 88 12 C94 24 70 34 52 30Z"/><circle cx="48" cy="27" r="7"/><path d="M44 32 L30 66 L38 62 L46 34Z M52 32 L66 66 L58 62 L50 34Z"/></svg>
  <h3>Close friends wishing<br>to give unique gifts</h3>
  <a class="btn-outline" href="#">Click here</a>
</div>
<div class="abs segment seg-moms">
  <svg width="84" height="78" viewBox="0 0 84 78" fill="none" stroke="#fff" stroke-width="3.5"><path d="M10 12h8l6 28h44 C70 22 58 12 44 12 L44 40"/><path d="M24 40 C26 52 66 52 68 40"/><circle cx="30" cy="64" r="8"/><circle cx="62" cy="64" r="8"/></svg>
  <h3>Moms with new born<br>baby personalized gifts</h3>
  <a class="btn-outline" href="#">Click here</a>
</div>

<section class="abs products"></section>
<h2 class="abs products-title">Our Products</h2>
<div class="abs slider-arrows">
  <svg width="14" height="22" viewBox="0 0 14 22" fill="none" stroke="#999" stroke-width="2"><path d="M11 2 L3 11 L11 20"/></svg>
  <svg width="14" height="22" viewBox="0 0 14 22" fill="none" stroke="#999" stroke-width="2"><path d="M3 2 L11 11 L3 20"/></svg>
</div>

<article class="abs card" style="left:107px">
  <div class="card-img" role="img" aria-label="Photo of a grey pillow embroidered with a name in light blue" style="background:linear-gradient(135deg,#6f6f6f,#9a9a9a 60%,#b7d6e6)"></div>
  <h4>Embroidered Pillows</h4><p class="sub">sociosqu ad litora torquent conubia</p>
  <div class="card-foot"><span class="price">$25.99</span><a class="btn-shop" href="#">Shop Now</a></div>
</article>
<article class="abs card" style="left:361px">
  <div class="card-img" role="img" aria-label="Photo of white and navy towels embroidered with names" style="background:linear-gradient(135deg,#e8e4ea,#7a4a7e 55%,#23315e)"></div>
  <h4>Towels</h4><p class="sub">sociosqu ad litora torquent conubia</p>
  <div class="card-foot"><span class="price">$25.99</span><a class="btn-shop" href="#">Shop Now</a></div>
</article>
<article class="abs card" style="left:617px">
  <div class="card-img" role="img" aria-label="Photo of coral and white bathrobes embroidered with a name" style="background:linear-gradient(135deg,#c98074,#ef7a6c 50%,#f1eeee)"></div>
  <h4>Bathrobes</h4><p class="sub">sociosqu ad litora torquent conubia</p>
  <div class="card-foot"><span class="price">$25.99</span><a class="btn-shop" href="#">Shop Now</a></div>
</article>
<article class="abs card" style="left:869px">
  <div class="card-img" role="img" aria-label="Photo of purple and white baby towels with embroidered names" style="background:linear-gradient(135deg,#8a6c98,#e9e6ec 55%,#cfc7d3)"></div>
  <h4>Baby gifts</h4><p class="sub">sociosqu ad litora torquent conubia</p>
  <div class="card-foot"><span class="price">$25.99</span><a class="btn-shop" href="#">Shop Now</a></div>
</article>

<svg class="abs testi-bg" viewBox="0 0 1200 520" preserveAspectRatio="none">
  <path d="M0,26 Q420,-4 760,22 T1200,14 L1200,520 L0,520 Z" fill="#b9964f"/>
  <path d="M380,12 Q800,4 1200,36" fill="none" stroke="#fff" stroke-width="4"/>
  <path d="M0,470 Q420,420 820,440 T1200,430 L1200,520 L0,520 Z" fill="#8a8a8a"/>
  <path d="M0,456 Q400,402 820,428" fill="none" stroke="#fff" stroke-width="4" opacity=".9"/>
</svg>
<h2 class="abs testi-title">Testimonials</h2>
<svg class="abs arrow-big" style="left:122px" width="24" height="40" viewBox="0 0 24 40" fill="none" stroke="#fff" stroke-width="3"><path d="M20 3 L5 20 L20 37"/></svg>
<svg class="abs arrow-big" style="left:1104px" width="24" height="40" viewBox="0 0 24 40" fill="none" stroke="#fff" stroke-width="3"><path d="M4 3 L19 20 L4 37"/></svg>
<blockquote class="abs quote" style="left:163px">
  <p><span class="mark">“</span>Ut nisi erat fermentum vel congue id euismod in elit Fusce ultricies orci ac feugiat suscipit leo massa sodales velit et scelerisque mi tortor</p>
  <div class="author">By Author Name <span class="stars">☆☆☆☆</span></div>
</blockquote>
<blockquote class="abs quote" style="left:640px">
  <p><span class="mark">“</span>Ut nisi erat fermentum vel congue id euismod in elit Fusce ultricies orci ac feugiat suscipit leo massa sodales velit et scelerisque mi tortor</p>
  <div class="author">By Author Name <span class="stars">☆☆☆☆</span></div>
</blockquote>

<footer class="abs footer" style="top:2330px;height:452px"></footer>
<div class="abs fcol" style="left:106px;top:2420px">
  <h5>MY ACCOUNT</h5>
  <ul><li>Privacy Policy</li><li>Your Account</li><li>Advanced Search</li><li>Contact Us</li></ul>
</div>
<div class="abs fcol" style="left:310px;top:2420px">
  <h5>COMPANY</h5>
  <ul><li>About Us</li><li>Contact Us</li><li>Franchise</li><li>New Arrivals</li><li>Finance</li></ul>
</div>
<div class="abs fcol" style="left:488px;top:2420px;color:#fff">
  <h5>CONTACT US</h5>
  <div class="contact-row">
    <svg width="16" height="22" viewBox="0 0 16 22" fill="#fff"><path d="M8 0C3.6 0 0 3.5 0 7.8 0 13.6 8 22 8 22s8-8.4 8-14.2C16 3.5 12.4 0 8 0zm0 11a3.2 3.2 0 110-6.4A3.2 3.2 0 018 11z"/></svg>
    <span>412 Harbor Loom Avenue Suite B12<br>Fairmont, NV 80231</span>
  </div>
  <div class="contact-row">
    <svg width="18" height="14" viewBox="0 0 18 14" fill="#fff" style="margin-top:4px"><path d="M0 0h18v14H0z"/><path d="M1 1l8 6 8-6" fill="none" stroke="#8a8a8a" stroke-width="1.5"/></svg>
    <span>Silver.needle.studio@mailbox.example</span>
  </div>
  <div class="contact-row">
    <svg width="18" height="18" viewBox="0 0 18 18" fill="#fff"><path d="M4 0l3 4-2 2c1 2.5 3 4.5 5.5 5.5l2-2 4 3-2 3.5C8 16 2 10 .5 3.5z"/></svg>
    <span>+966 55 312 0976</span>
  </div>
</div>
<div class="abs fcol" style="left:807px;top:2420px">
  <h5>SIGN UP NEWSLETTER</h5>
  <div class="newsletter-input">EMAIL ADDRESS</div>
  <a class="btn-subscribe" href="#">Subscribe</a>
  <div class="pay"><span></span><span></span><span></span><span></span></div>
</div>
<div class="abs divider"></div>
<p class="abs copyright">© 2017 Company Name All right reserved  Term of Use</p>

</body>
</html>
```